New Design for Accounting Firm

CLIENT NAME: Corvantis
CURRENT WEBSITE: www.corvantisgroup-example.com.au

CLIENTS THE CLIENT LIKES:
http://velmarook.example.se/
http://www.tralvexio.example.biz/index.php
http://www.brindlequo.example.co.uk/
http://www.nerovaskellintrust.example.org/

COLOUR THEMES:
Colour theme to reflect the logo, with a leaning to blue in Accounting & Audit sections and green in Super section.

LOOK AND FEEL:
The look and feel needs to reflect an accessible culture and contemporary sensibility while still communicating our experience and stability as a professional company.

ABOUT:
The concept of 'Corvantis' is integral to our identity. Definition: 'The connection of creative ideas from a group of diverse individuals, applied with the end aim of solving practical problems'. See ''About Us'' on our website for more.

OTHER DETAILS:
Our three divisions (and service areas within each division) must be easily navigated as they related to very different users of the site. Two client sign in sections (Accounting & Super) must be easily distinguished to avoid user confusion.

MENU STRUCTURE:
* About
- includes history, values, our people, community etc
* Accounting & Advisory
- About
- Services
- Tax & Accounting
- Business Advisory
- Family Wealth Management
- Client Sign In
- Calculators
* Audit & Assurance
- About
- Services
* Corvantis Super
- About
- Individuals
- Services
- Advisers
- Services
- Portal Sign In
- Calculators
* Careers
* Newsletters
* Contact

REQUIREMENTS:
- Layered PSD form home and content pages
- No coding required, we use our own CMS to insert XHTML files into.
Updates

Hi Guys,

The client has asked for a non-cliche'd images in the design. If you'd like to try again with some images that represent the business but aren't your standard boring accounting-looking people, then please do! Cliche is a killer in design - please pump some creativity in!

Cheers,
Ted.

Reason: GUYS - PLEASE LISTEN TO THESE COMMENTS - I'VE SAID THEM TWICE NOW AND PEOPLE ARE STILL POSTING PROJECTS WITH CLICHED AND OBVIOUS ACCOUTNING TYPE IMAGES. USE YOUR CREATIVITY AND POST A DESIGN THAT IS OUTSIDE THE BOX WITH REGARDS TO THE IMAGES YOU ARE USING.

Reason: I am waiting to hear back from the client on their decision.

```html
<!DOCTYPE html>
<html lang="en">
<head>
<meta charset="utf-8">
<title>Corvantis – Home</title>
<link rel="stylesheet" href="https://fonts.googleapis.com/css2?family=Arimo:wght@400;700&family=Didact+Gothic&family=PT+Serif&display=swap">
<style>
:root{
  --brand-blue:#1f72b8;
  --brand-green:#5bb85f;
  --band-top:#2b97e0;
  --band-bottom:#1269b6;
  --ink:#3a3a3a;
  --heading:#4a4a4a;
  --link:#1b4f8c;
  --list-link:#3a6aa8;
  --footer:#0e1722;
  --footer-text:#d9dde2;
  --muted:#9aa3ad;
}
*{box-sizing:border-box;margin:0;padding:0}
html,body{width:1072px;height:1200px;overflow:hidden;background:#fff}
body{font-family:"Arimo",Arial,sans-serif;color:var(--ink)}
.page{position:relative;width:1072px;height:1200px;overflow:hidden;background:linear-gradient(#f6f6f6,#fff 130px)}
.abs{position:absolute}

.brand{display:flex;align-items:center;gap:10px}
.brand-mark{width:44px;height:44px;background:var(--brand-blue)}
.brand-name{font-family:"Didact Gothic",sans-serif;font-size:52px;color:var(--brand-blue);line-height:1;letter-spacing:-1px}
.header-brand{left:128px;top:22px}

.client-login{left:871px;top:32px;width:89px;height:25px;border-radius:3px;background:linear-gradient(#7fd67a,#3fae45);border:1px solid #3b9d3f;color:#fff;font:700 10.5px "Arimo",sans-serif;display:flex;align-items:center;justify-content:center;letter-spacing:.2px}

.main-nav{left:116px;top:100px;display:flex;align-items:center;font-family:"Didact Gothic",sans-serif;font-size:13.5px;color:#222}
.main-nav a{color:inherit;text-decoration:none;padding:0 16px;border-left:1px solid #c9c9c9;line-height:17px}
.main-nav a:nth-child(2){border-left:none}
.main-nav a.current{border:none;background:#fff;padding:4px 14px;box-shadow:0 3px 3px rgba(0,0,0,.35);margin-right:2px}

.hero{left:0;top:132px;width:1072px;height:231px;background:linear-gradient(var(--band-top),var(--band-bottom))}
.hero-photo{left:170px;top:11px;width:404px;height:210px;border:4px solid #fff;background:linear-gradient(120deg,#e9e4dc,#cfc6b8 40%,#8b8f99 70%,#d8d2ca)}
.hero-arrow{width:40px;height:40px;border-radius:50%;background:linear-gradient(#fff,#cfd3d8);border:2px solid #e7e7e7;box-shadow:0 2px 4px rgba(0,0,0,.35);top:88px}
.hero-arrow svg{position:absolute;left:9px;top:9px}
.hero-text{left:598px;top:32px;width:320px;font-family:"PT Serif",serif;font-size:18.5px;line-height:25.5px;color:#fff;white-space:nowrap}
.hero-button{left:632px;top:168px;width:205px;height:38px;background:linear-gradient(#fff,#e4e6e8);border:1px solid #cfd4d8;box-shadow:0 0 0 3px rgba(255,255,255,.35),0 2px 4px rgba(0,0,0,.3);font:400 15px "Arimo",sans-serif;color:#204a1f;display:flex;align-items:center;justify-content:center}

h2{font-family:"Arimo",sans-serif;font-weight:400;font-size:20px;color:var(--heading)}
h3{font-family:"Arimo",sans-serif;font-weight:400;font-size:17px;color:var(--heading)}
p.body{font-size:10.3px;line-height:17px;color:var(--ink)}

.welcome{left:121px;top:403px;width:455px}
.welcome h2{margin-bottom:12px}
.welcome p{margin-bottom:17px}
.tour{left:119px;top:606px;font-size:11px;color:#7a1040;text-decoration:underline}

.testimonial{left:643px;top:402px;width:300px}
.quote-mark{font-family:"PT Serif",serif;font-size:56px;color:#c7c7c7;line-height:1}
.testimonial-text{white-space:nowrap}
.author{left:650px;top:556px;font-size:12px;color:#444}

.col{top:654px}
.col h3{margin-bottom:12px}
.about-col{left:120px;width:240px}
.about-col p{font-size:10.3px;line-height:17px;white-space:nowrap}
.bullets{list-style:none}
.bullets li{position:relative;padding-left:19px}
.bullets li::before{content:"";position:absolute;left:0;width:6px;height:6px;border:1px solid #b9c0c6;border-radius:50%}
.why-col{left:405px;width:230px}
.why-col li{font-size:10.3px;line-height:24.7px;color:var(--list-link)}
.why-col li::before{top:8px}
.do-col{left:681px;width:200px}
.do-col li{font-size:13px;line-height:23px;color:var(--list-link);text-decoration:underline}
.do-col li::before{top:8px}

.partners{left:122px;top:877px;width:839px;height:55px;background:#fff;border:1px solid #e1e1e1;box-shadow:0 1px 3px rgba(0,0,0,.12);padding:4px}
.partners-inner{width:100%;height:100%;background:repeating-linear-gradient(90deg,#ececec 0 1px,#e2e2e2 1px 2px);display:flex;align-items:center;position:relative}
.partners-label{position:absolute;left:4px;top:4px;font-family:"PT Serif",serif;font-style:italic;font-weight:400;font-size:13.5px;line-height:17px;color:#555}
.partners-arrow{position:absolute;top:17px;width:16px;height:16px;background:#9a9a9a;border:1px solid #777;color:#fff;font:700 12px/13px "Arimo",sans-serif;text-align:center}
.partner{position:absolute;top:15px;font-family:"Arimo",sans-serif;font-size:17px;color:#3a3a3a;display:flex;align-items:center;gap:6px}
.partner i{display:block;width:12px;height:12px;background:#8a8a8a}

.footer{left:0;top:969px;width:1072px;height:231px;background:var(--footer)}
.footer h4{font-family:"Arimo",sans-serif;font-weight:400;font-size:14px;color:#b7bec6;margin-bottom:12px}
.footer ul{list-style:none}
.footer li{position:relative;padding-left:20px;font-size:9.5px;font-weight:700;line-height:18.7px;color:var(--footer-text)}
.footer li::before{content:"";position:absolute;left:0;top:6px;border-left:7px solid #cfd5db;border-top:3.5px solid transparent;border-bottom:3.5px solid transparent}
.footer .services li{text-decoration:underline}
.footer-nav{left:128px;top:36px}
.footer-services{left:318px;top:36px}
.footer-brand{left:666px;top:55px}
.footer-brand .brand-name{font-size:52px}
.copyright{left:657px;top:148px;font-size:10.5px;color:#c9cfd5}
</style>
</head>
<body>
<div class="page">

  <header>
    <div class="abs brand header-brand"><span class="brand-mark"></span><span class="brand-name">Corvantis</span></div>
    <a class="abs client-login">CLIENT LOGIN</a>
    <nav class="abs main-nav">
      <a class="current">Home</a>
      <a>About Us</a>
      <a>Accounting &amp; Advisory</a>
      <a>Audit &amp; Assurance</a>
      <a>Corvantis Super</a>
      <a>Careers</a>
      <a>Newsletters</a>
      <a>Contact</a>
    </nav>
  </header>

  <section class="abs hero">
    <div class="abs hero-arrow" style="left:119px"><svg width="20" height="20" viewBox="0 0 20 20"><path d="M13 3 6 10l7 7" fill="none" stroke="#333" stroke-width="4"/></svg></div>
    <div class="abs hero-photo" role="img" aria-label="Photo of a smiling businessman in a light suit with colleagues talking in the background"></div>
    <p class="abs hero-text">The connection of creative ideas<br>from a group of diverse individuals,<br>applied with the end aim of solving<br>practical problems</p>
    <a class="abs hero-button">Click to View More..</a>
    <div class="abs hero-arrow" style="left:917px"><svg width="20" height="20" viewBox="0 0 20 20"><path d="M7 3l7 7-7 7" fill="none" stroke="#333" stroke-width="4"/></svg></div>
  </section>

  <section class="abs welcome">
    <h2>Welcome to Corvantis</h2>
    <p class="body">It is a long established fact that a reader will be distracted by the readable content of a page when looking at its layout. The point of using Lorem Ipsum is that it has a more-or-less normal distribu-tion of letters, as opposed to using 'Content here,</p>
    <p class="body">It is a long established fact that a reader will be distracted by the readable content of a page when looking at its layout. The point of using Lorem Ipsum is that it has a more-or-less normal distribu-tion of letters, as opposed to using 'Content here,The point of using Lorem Ipsum is that it has a more-or-less normal distribution of letters, as opposed to using 'Content here,</p>
  </section>
  <a class="abs tour">Take a tour to learn more </a>

  <section class="abs testimonial">
    <h2>What people are saying:</h2>
  </section>
  <span class="abs quote-mark" style="left:612px;top:421px">&ldquo;</span>
  <p class="abs body testimonial-text" style="left:650px;top:442px">It is a long established fact that a reader will be distracted<br>by the readable content of a page when looking at its<br>layout. The point of using Lorem Ipsum is that it has a<br>more-or-less normal distribution of letters, as opposed to<br>using 'Content here,</p>
  <p class="abs author">Mr.Alden Frey,Norwick Company</p>
  <span class="abs quote-mark" style="left:861px;top:551px">&rdquo;</span>

  <section class="abs col about-col">
    <h3>About Us</h3>
    <p>For the people who work in our firm, 'Corvantis'<br>means that we use of our diverse skills, experience<br>and backgrounds to produce creative yet consistent<br>solutions to the practical challenges which our<br>clients encounter.<br>We recognise that, with the complexities of today's<br>financial world, a lot of people aren't sure where to<br>begin to get systematic analysis, expert knowledge<br>and the right advice. Many people are anxious to<br>get their personal ....</p>
  </section>
  <section class="abs col why-col">
    <h3>Why We Are?</h3>
    <ul class="bullets">
      <li>Expert business know how</li>
      <li>Excellent corporate relationships</li>
      <li>Leading edge technology</li>
      <li>Simple but effective solutions</li>
      <li>An understanding of our clients and<br>how to meet their requirements</li>
    </ul>
  </section>
  <section class="abs col do-col">
    <h3>What We Do?</h3>
    <ul class="bullets">
      <li>Integrated Services Plan</li>
      <li>Completion Dates</li>
      <li>Agreed Annual Timeline</li>
      <li>Algorithmic traders</li>
      <li style="text-decoration:none">Quoted Fee</li>
      <li>Completion Dates</li>
    </ul>
  </section>

  <section class="abs partners">
    <div class="partners-inner">
      <span class="partners-label">We're the<br>trusted partner of</span>
      <span class="partners-arrow" style="left:148px">&laquo;</span>
      <span class="partner" style="left:190px">Keltaro</span>
      <span class="partner" style="left:335px">Larvessa</span>
      <span class="partner" style="left:498px">Quintavel</span>
      <span class="partner" style="left:668px"><i></i>Fennick</span>
      <span class="partners-arrow" style="left:800px">&raquo;</span>
    </div>
  </section>

  <footer class="abs footer">
    <div class="abs footer-nav">
      <h4>Main Navigation</h4>
      <ul><li>About Us</li><li>Services</li><li>Who We Are</li><li>Contact Us</li><li>Sitemap</li></ul>
    </div>
    <div class="abs footer-services services">
      <h4>Our Services</h4>
      <ul><li>Integrated Services Plan</li><li>Completion Dates</li><li>Agreed Annual Timeline</li><li>Algorithmic traders</li><li style="text-decoration:none">Quoted Fee</li><li>Completion Dates</li></ul>
    </div>
    <div class="abs brand footer-brand"><span class="brand-mark"></span><span class="brand-name">Corvantis</span></div>
    <p class="abs copyright">Copyright &copy; Corvantis Group 2011 &nbsp; | &nbsp;Terms and Conditions</p>
  </footer>

</div>
</body>
</html>
```